Lumora Dwellings

Design a stylish Business card- we would like a businness card design that suits plastic business cards. Our card needs to show that we are tech savy and technology based so the design is crucial.

Target Market(s)

22-40

Industry/Entity Type

Plastic

Requirements
Must have
• attached is our logo. also double sided card would be nice.
my details

Tobias Fenwright
Director
0471596234
www.lumoradwellings.com.au
17 Ashcombe Lane, West Perth

```html
<!DOCTYPE html>
<html lang="en">
<head>
<meta charset="utf-8">
<title>Lumora Dwellings – Business Card</title>
<link rel="stylesheet" href="https://fonts.googleapis.com/css2?family=Source+Sans+3:wght@400;600;700&family=Tinos:ital,wght@1,700&display=swap">
<style>
  :root{
    --page:#e9e7e4;
    --card-dark:#0c0d0f;
    --card-mid:#2b2e33;
    --sky:#3bbde6;
    --teal:#2a6f86;
    --steel:#4a8fae;
    --silver:#b9bcc0;
    --white:#ffffff;
    --shadow:rgba(0,0,0,.35);
  }
  *{margin:0;padding:0;box-sizing:border-box}
  html,body{width:1077px;height:1200px;overflow:hidden;background:var(--page)}
  .stage{position:relative;width:1077px;height:1200px}
  .card{position:absolute;width:780px;height:446px;border-radius:22px;overflow:hidden;
        box-shadow:0 8px 18px var(--shadow);background:var(--card-dark)}
  .card-front{left:54px;top:128px}
  .card-back{left:231px;top:614px}
  .card-art{position:absolute;inset:0;width:100%;height:100%}
  .brand{position:absolute;display:flex;align-items:center;gap:16px}
  .brand-mark{width:64px;height:64px;background:var(--silver);border-radius:6px;flex:none}
  .brand-name{font-family:"Source Sans 3",sans-serif;font-weight:700;font-size:50px;line-height:1;color:var(--steel);text-transform:uppercase;letter-spacing:1px;white-space:nowrap}
  .front-brand{left:120px;top:168px}
  .back-brand{left:130px;top:106px}
  .holder{position:absolute;right:62px;top:22px;color:var(--white)}
  .holder-name{font-family:"Tinos",serif;font-style:italic;font-weight:700;font-size:24px}
  .holder-role{font-family:"Source Sans 3",sans-serif;font-size:19px;margin-top:-2px}
  .address{position:absolute;left:68px;top:330px;font-family:"Source Sans 3",sans-serif;font-size:23px;color:var(--white);line-height:1.3}
  .address-line{display:flex;align-items:center;gap:8px}
  .address-line.indent{padding-left:30px}
  .icon{width:22px;height:22px;flex:none}
  .contacts{position:absolute;left:60px;top:305px;font-family:"Source Sans 3",sans-serif;font-size:23px;color:var(--white);list-style:none;line-height:1.38}
  .contacts li{display:flex;align-items:center;gap:8px}
</style>
</head>
<body>
<div class="stage">

  <section class="card card-front">
    <svg class="card-art" viewBox="0 0 780 446" preserveAspectRatio="none">
      <defs>
        <linearGradient id="frontTexture" x1="0" y1="0" x2="1" y2="1">
          <stop offset="0" stop-color="#3a3d42"/>
          <stop offset=".5" stop-color="#25272b"/>
          <stop offset="1" stop-color="#17181b"/>
        </linearGradient>
        <linearGradient id="frontTop" x1="0" y1="0" x2="1" y2="0">
          <stop offset="0" stop-color="#3f5a66"/>
          <stop offset=".55" stop-color="#2e8fb0"/>
          <stop offset="1" stop-color="#3bbde6"/>
        </linearGradient>
        <linearGradient id="frontBottom" x1="0" y1="0" x2="1" y2="0">
          <stop offset="0" stop-color="#0e1012"/>
          <stop offset=".6" stop-color="#1e4b5c"/>
          <stop offset="1" stop-color="#3bbde6"/>
        </linearGradient>
      </defs>
      <rect width="780" height="446" fill="url(#frontTexture)" role="img" aria-label="Dark monochrome textured photograph background"/>
      <path d="M0 0H780V70C640 40 560 120 400 120C260 120 150 60 0 50Z" fill="url(#frontTop)"/>
      <path d="M0 50C150 60 260 120 400 120C560 120 640 40 780 70V84C640 58 560 140 400 140C250 140 140 78 0 68Z" fill="var(--silver)"/>
      <path d="M0 300C90 260 220 250 330 300C420 340 520 420 560 446H0Z" fill="url(#frontBottom)"/>
      <path d="M0 288C100 246 230 236 340 290C440 340 530 420 570 446H548C510 420 420 352 330 306C220 254 100 262 0 304Z" fill="var(--silver)"/>
      <path d="M560 446C620 420 700 360 780 330V446Z" fill="url(#frontTop)"/>
    </svg>
    <div class="holder">
      <div class="holder-name">Tobias Fenwright</div>
      <div class="holder-role">Director</div>
    </div>
    <div class="brand front-brand">
      <div class="brand-mark"></div>
      <div class="brand-name">Lumora Dwellings</div>
    </div>
    <div class="address">
      <div class="address-line">
        <svg class="icon" viewBox="0 0 24 24"><path d="M12 3L2 12h3v9h5v-6h4v6h5v-9h3z" fill="var(--white)"/></svg>
        17 Ashcombe Lane,
      </div>
      <div class="address-line indent">West Perth</div>
    </div>
  </section>

  <section class="card card-back">
    <svg class="card-art" viewBox="0 0 780 446" preserveAspectRatio="none">
      <defs>
        <linearGradient id="backBottom" x1="0" y1="0" x2="1" y2="0">
          <stop offset="0" stop-color="#0c0d0f"/>
          <stop offset=".55" stop-color="#1d4756"/>
          <stop offset="1" stop-color="#3bbde6"/>
        </linearGradient>
      </defs>
      <rect width="780" height="446" fill="var(--card-dark)"/>
      <path d="M0 280C120 220 250 230 360 260C480 292 600 300 780 290V446H0Z" fill="url(#backBottom)"/>
      <path d="M0 262C120 204 250 214 360 244C480 276 600 284 780 274V292C600 302 480 294 360 262C250 232 120 222 0 282Z" fill="var(--silver)"/>
      <path d="M480 446C600 410 700 340 780 290V446Z" fill="var(--sky)" opacity=".9"/>
      <path d="M470 446C590 410 690 340 780 282V292C700 346 600 416 488 446Z" fill="var(--silver)"/>
    </svg>
    <div class="brand back-brand">
      <div class="brand-mark"></div>
      <div class="brand-name">Lumora Dwellings</div>
    </div>
    <ul class="contacts">
      <li>
        <svg class="icon" viewBox="0 0 24 24"><circle cx="12" cy="12" r="10" fill="none" stroke="var(--white)" stroke-width="2"/><path d="M9 7l2 3-1 1c.6 1.4 1.6 2.4 3 3l1-1 3 2-1 2c-4 0-8-4-8-8z" fill="var(--white)"/></svg>
        0471596234
      </li>
      <li>
        <svg class="icon" viewBox="0 0 24 24"><rect x="2" y="5" width="20" height="14" fill="none" stroke="var(--white)" stroke-width="2"/><path d="M2 5l10 8 10-8" fill="none" stroke="var(--white)" stroke-width="2"/></svg>
        info@lumoradwellings.com.au
      </li>
      <li>
        <svg class="icon" viewBox="0 0 24 24"><circle cx="12" cy="12" r="10" fill="none" stroke="var(--white)" stroke-width="2"/><path d="M2 12h20M12 2c3 3 3 17 0 20M12 2c-3 3-3 17 0 20" fill="none" stroke="var(--white)" stroke-width="1.6"/></svg>
        www.lumoradwellings.com.au
      </li>
    </ul>
  </section>

</div>
</body>
</html>
```